3 banner themes for healthy foods supplements

Who you are
You are a top professional designer. You eat, sleep and breathe banners. You have them for breakfast, lunch and dinner. You have created so many high quality banners that you stopped counting.
Who we are
We are selling premium nutritional supplements.

Deliverables
We need to design 3 different banner themes, each in the following formats:
- Vertical rectangle: 240 x 400
- Mobile leaderboard: 320 x 50
- Banner: 468 x 60
- Leaderboard: 728 x 90
- Square: 250 x 250
- Small square: 200 x 200
- Large rectangle: 336 x 280
- Inline rectangle: 300 x 250
- Skyscraper: 120 x 600
- Wide skyscraper: 160 x 600
- Half-page: 300 x 600
- Large leaderboard: 970x90
- Large mobile banner: 320 x 100
- Billboard: 970 x 250
- Portrait: 300 x 1050

To give us a taste of your design skills, we invite you to submit one format (300 x 250) of each of the 3 different banner themes described below before we finally give you the green light and award you. Once awarded you should deliver all 3 themes with all above mentioned banner formats.

The final deliverable shall be editable .psd files.

Our products
The products we are advertising are organic, raw, vegan, premium nutritional supplements, such as algae powder, wheat grass powder and goji berries. The products stand to support a healthy life style. Please have a look at our shop. It is in German, but you get the gist. http://www.merolina.-shop.example

The design
We would describe the style of the banners as follows:
- Premium
- Joyful
- White background
- Minimalistic

Each banner theme shall advertise the following messages about the products:
- Product name (chlorella algae powder , wheatgrass powder, goji berries)
- healthy
- 100 % vegan, raw and organic
- 100% natural
- premium product

Each of the above attributes can be represented with labels of different colours, similar to the attached sample files. We like the colour combination of the labels on this banner a lot.
All 3 themes shall contain our logo which you find attached to this job description. The logo shall be visible, but not too prominent.

The only difference between the 3 different themes shall be the product photo and the product name. All other elements on the banner shall be the same.

Theme A
This theme advertises algae powder, such as chlorella algae. The product photo is attached and should of course appear prominently on the banner.

Theme B
This theme advertises wheat grass powder. The product photo is attached and should of course appear prominently on the banner.

Theme C
This theme advertises goji berries. The product photo is attached and should of course appear prominently on the banner.

Target Market(s)

Health conscious people.

Industry/Entity Type

It Professional

Font styles to use
Sans Serif

Colors
00a990
a54499
f37122
fbed22
0692cd
9bcb3b
ffc214

Requirements
Must have
• - product image as per in the attachment
• - logo
• - bright, clear, joyful colors
Should not have
• - heavy dark colors
• - frame

```html
<!DOCTYPE html>
<html lang="en">
<head>
<meta charset="utf-8">
<title>Healthy food supplements – banner themes</title>
<link rel="stylesheet" href="https://fonts.googleapis.com/css2?family=Ubuntu&family=ABeeZee&family=Comfortaa:wght@300&display=swap">
<style>
  :root {
    --stage: #373233;
    --white: #ffffff;
    --teal: #00a990;
    --purple: #a54499;
    --orange: #f37122;
    --lemon: #fbed22;
    --blue: #0692cd;
    --lime: #9bcb3b;
    --amber: #ffc214;
    --algae: #2f5a45;
    --wheat: #c4c98a;
    --goji: #e0452a;
  }
  * { box-sizing: border-box; margin: 0; padding: 0; }
  html, body {
    width: 1200px; height: 1000px; overflow: hidden;
    background: var(--stage);
  }
  .board { position: relative; width: 1200px; height: 1000px; }

  .theme-title {
    position: absolute; top: 259px; width: 336px;
    text-align: center; color: var(--white);
    font: 30px/36px "Ubuntu", sans-serif;
  }

  .banner {
    position: absolute; width: 336px; height: 280px;
    background: var(--white); overflow: hidden;
    box-shadow: 4px 4px 5px rgba(0,0,0,.75);
  }
  .product-photo { position: absolute; left: 0; top: 0; width: 336px; }
  .theme-a .product-photo {
    height: 240px;
    background: radial-gradient(ellipse 70% 60% at 65% 40%, var(--algae), rgba(47,90,69,.55) 60%, rgba(255,255,255,0) 100%);
  }
  .theme-b .product-photo {
    height: 250px;
    background: radial-gradient(ellipse 75% 65% at 50% 45%, var(--wheat), rgba(196,201,138,.5) 65%, rgba(255,255,255,0) 100%);
  }
  .theme-c .product-photo {
    height: 150px;
    background: radial-gradient(ellipse 80% 75% at 60% 20%, var(--goji), rgba(224,69,42,.6) 60%, rgba(255,255,255,0) 100%);
  }

  .brand-box {
    position: absolute; left: 23px; top: 65px; width: 114px; height: 69px;
    background: var(--lemon);
    display: flex; align-items: center; justify-content: center;
    color: var(--teal); font: 300 18px "Comfortaa", sans-serif;
  }
  .product-name {
    position: absolute; left: 137px; top: 65px; width: 199px; height: 69px;
    background: var(--lime); color: var(--white);
    display: flex; align-items: center; justify-content: center;
    text-align: center; font: 28px/29px "ABeeZee", sans-serif;
    white-space: nowrap;
  }
  .label {
    position: absolute; right: 0; height: 38px;
    color: var(--white); font: 300 18px "Comfortaa", sans-serif;
    display: flex; align-items: center; justify-content: center;
    white-space: nowrap;
    box-shadow: -3px 5px 6px rgba(0,0,0,.3);
  }
  .label-vegan { top: 142px; left: 48px; background: var(--purple); font-size: 17px; }
  .label-natural { top: 187px; left: 102px; background: var(--amber); }
  .label-premium { top: 232px; left: 147px; background: var(--blue); }

  .buy-button {
    position: absolute; left: 22px; top: 237px; width: 104px; height: 34px;
    border-radius: 17px; background: var(--orange); color: var(--lemon);
    font: bold 17px Arial, Helvetica, sans-serif;
    display: flex; align-items: center; justify-content: center;
  }
</style>
</head>
<body>
<div class="board">
  <h2 class="theme-title" style="left:78px">Theme A</h2>
  <h2 class="theme-title" style="left:434px">Theme B</h2>
  <h2 class="theme-title" style="left:781px">Theme C</h2>

  <section class="banner theme-a" style="left:78px; top:332px">
    <div class="product-photo" role="img" aria-label="Dark green chlorella algae powder scattered on white"></div>
    <div class="brand-box">Alvora</div>
    <div class="product-name">chlorella<br>algae powder</div>
    <div class="label label-vegan">100 % vegan, raw and organic</div>
    <div class="label label-natural">100% natural healthy</div>
    <div class="label label-premium">premium product</div>
    <div class="buy-button">Buy Now!</div>
  </section>

  <section class="banner theme-b" style="left:434px; top:332px">
    <div class="product-photo" role="img" aria-label="Pale green wheatgrass powder heaped on white"></div>
    <div class="brand-box">Alvora</div>
    <div class="product-name">wheatgrass<br>powder</div>
    <div class="label label-vegan">100 % vegan, raw and organic</div>
    <div class="label label-natural">100% natural healthy</div>
    <div class="label label-premium">premium product</div>
    <div class="buy-button">Buy Now!</div>
  </section>

  <section class="banner theme-c" style="left:794px; top:330px">
    <div class="product-photo" role="img" aria-label="Pile of dried red goji berries"></div>
    <div class="brand-box">Alvora</div>
    <div class="product-name">goji berries</div>
    <div class="label label-vegan">100 % vegan, raw and organic</div>
    <div class="label label-natural">100% natural healthy</div>
    <div class="label label-premium">premium product</div>
    <div class="buy-button">Buy Now!</div>
  </section>
</div>
</body>
</html>
```